Website Design for A Leading Live Casino Software Provider

We provide live casino software to other land based and online gaming establishments. We are a B2B provider.

```html
<!DOCTYPE html>
<html lang="en">
<head>
<meta charset="utf-8">
<title>Crown Table Studios — Live Casino Software</title>
<link rel="stylesheet" href="https://fonts.googleapis.com/css2?family=Ubuntu:wght@400;500&family=Arimo:ital,wght@0,400;1,400&display=swap">
<style>
:root{
  --page:#d6d6d6;
  --page-light:#e4e4e4;
  --navy:#0e3467;
  --navy-deep:#08234a;
  --navy-mid:#164a86;
  --navy-line:#0b2c57;
  --brand-blue:#1f5fa0;
  --ink:#1c2a3a;
  --tagline:#1b3f77;
  --white:#ffffff;
  --accent:#9a9cf2;
  --nav-top:#f4f4f4;
  --nav-bottom:#cfcfcf;
  --tile-top:#cfcfcf;
  --tile-bottom:#a9a9a9;
  --arrow:#b9c3d1;
}
*{box-sizing:border-box;margin:0;padding:0}
html,body{width:1004px;height:1200px;overflow:hidden}
body{
  position:relative;
  background:linear-gradient(180deg,var(--page-light),var(--page) 30%,var(--page));
  font-family:"Arimo",Arial,sans-serif;
  color:var(--ink);
}
.site-header{position:absolute;left:0;top:0;width:1004px;height:86px;
  background:repeating-linear-gradient(135deg,#e6e6e6 0 3px,#dcdcdc 3px 5px)}
.brand-name{position:absolute;left:26px;top:24px;font-family:"Ubuntu",sans-serif;font-weight:500;font-size:28px;color:var(--brand-blue);line-height:1}
.header-call{position:absolute;right:18px;top:52px;font-family:"Ubuntu",sans-serif;font-size:19px;color:var(--tagline)}
.header-rule{position:absolute;left:0;top:86px;width:1004px;height:12px;background:linear-gradient(180deg,var(--navy-mid),var(--navy-deep))}

.main-nav{position:absolute;left:0;top:100px;width:1004px;height:42px;display:flex;
  background:linear-gradient(180deg,var(--nav-top),var(--nav-bottom));border-top:1px solid #bdbdbd;border-bottom:1px solid #a8a8a8}
.main-nav a{display:flex;align-items:center;justify-content:center;height:100%;
  font-family:"Ubuntu",sans-serif;font-size:20px;color:#222;text-decoration:none;border-right:1px solid #a9a9a9;box-shadow:inset -1px 0 0 #fafafa}
.main-nav a:last-child{border-right:none}

.hero{position:absolute;left:0;top:142px;width:1004px;height:447px;
  background:radial-gradient(ellipse at 50% 40%,var(--navy-mid),var(--navy) 55%,var(--navy-deep))}
.hero-line{position:absolute;left:80px;width:844px;height:1px;background:rgba(160,190,230,.35)}
.hero-slide{position:absolute;left:148px;top:23px;width:708px;height:313px;
  background:radial-gradient(ellipse at 45% 35%,#6f6a66,#2a2624 50%,#0b0a0a 80%)}
.hero-caption{position:absolute;left:148px;top:285px;width:708px;height:47px;background:rgba(10,30,60,.7);padding:6px 14px}
.hero-caption h2{font-family:"Ubuntu",sans-serif;font-weight:400;font-size:17px;color:var(--white)}
.hero-caption p{font-size:12.5px;color:var(--white);padding-left:22px;margin-top:2px}
.hero-caption .hl{color:var(--accent)}
.hero-caption .love{color:#d78ad9}
.hero-thumbs{position:absolute;left:148px;top:338px;width:708px;height:92px;display:flex;border:1px solid #3a5e8c;background:#111}
.hero-thumbs div{flex:1;border-right:1px solid #333}
.hero-thumbs div:last-child{border-right:none}
.t1{background:linear-gradient(135deg,#3a3f45,#15181b)}
.t2{background:linear-gradient(160deg,#8b8784,#1a1716 60%,#a5262b)}
.t3{background:linear-gradient(180deg,#4a5260,#3a3a2a)}
.t4{background:linear-gradient(135deg,#f2f2f2,#cfcfcf)}
.t5{background:linear-gradient(135deg,#3d3a38,#121010)}
.arrow{position:absolute}

.band-gap{position:absolute;left:0;top:589px;width:1004px;height:17px;background:linear-gradient(180deg,#cfcfcf,#e0e0e0)}
.dealers{position:absolute;left:0;top:606px;width:1004px;height:167px;
  background:radial-gradient(ellipse at 50% 50%,var(--navy-mid),var(--navy) 60%,var(--navy-deep))}
.dealers h2{position:absolute;top:6px;width:100%;text-align:center;font-family:"Ubuntu",sans-serif;font-weight:400;font-size:19px;color:var(--white)}
.dealers h2 span,.dealers p span{color:var(--accent)}
.dealer-tile{position:absolute;top:35px;width:130px;height:98px;background:linear-gradient(180deg,var(--tile-top),var(--tile-bottom))}
.dealers p{position:absolute;top:141px;width:100%;text-align:center;font-size:13.5px;color:#c9d2df}

.panel{position:absolute;background:var(--navy);border:2px solid #b8b8b8;outline:1px solid var(--navy-line);color:var(--white)}
.panel h3{font-family:"Ubuntu",sans-serif;font-weight:400;font-size:20px}
.news{left:1px;top:788px;width:432px;height:234px}
.news h3{position:absolute;left:5px;top:24px}
.news ul{list-style:none;position:absolute;left:25px;top:68px}
.news li{font-size:12.5px;margin-bottom:14.4px;white-space:nowrap}
.news li span{color:var(--accent)}
.more{position:absolute;right:7px;bottom:6px;font-style:italic;font-size:12.5px}
.about{left:461px;top:788px;width:535px;height:194px}
.about h3{position:absolute;left:22px;top:24px}
.about p{position:absolute;left:14px;top:63px;width:505px;font-size:12.3px;line-height:15.5px;color:#e8edf4}

.site-footer{position:absolute;left:0;top:1107px;width:1004px;text-align:center}
.footer-call{font-family:"Ubuntu",sans-serif;font-size:18px;line-height:23px;color:#111}
.footer-rule{width:210px;height:1px;background:#555;margin:16px auto 6px}
.copyright{font-size:12px;color:#222}
</style>
</head>
<body>
<header class="site-header">
  <div class="brand-name">Crown Table Studios</div>
  <div class="header-call">Call Toll Free 1-xxx-xxx-xxxx and get a FREE Demo of our Software and Solutions</div>
</header>
<div class="header-rule"></div>

<nav class="main-nav">
  <a href="#" style="width:114px">Home</a>
  <a href="#" style="width:139px">About us</a>
  <a href="#" style="width:152px">Live games</a>
  <a href="#" style="width:161px">Our solutions</a>
  <a href="#" style="width:188px">News and events</a>
  <a href="#" style="width:115px">Videos</a>
  <a href="#" style="width:135px">Contact us</a>
</nav>

<section class="hero">
  <div class="hero-line" style="top:6px"></div>
  <div class="hero-slide" role="img" aria-label="Night photo of an illuminated casino city welcome sign with chips"></div>
  <div class="hero-caption">
    <h2>Transparent and Authentic Gaming Experience</h2>
    <p>Your Players will <span class="love">LOVE</span> the reliability of Vegas <span class="hl">quality</span> games transmitted <span class="hl">live</span>.</p>
  </div>
  <div class="hero-line" style="top:336px"></div>
  <div class="hero-thumbs">
    <div class="t1" role="img" aria-label="Server room thumbnail"></div>
    <div class="t2" role="img" aria-label="Casino sign thumbnail"></div>
    <div class="t3" role="img" aria-label="Celebrating winner thumbnail"></div>
    <div class="t4" role="img" aria-label="Rising growth chart thumbnail"></div>
    <div class="t5" role="img" aria-label="Live dealer thumbnail"></div>
  </div>
  <svg class="arrow" style="left:106px;top:184px" width="20" height="28" viewBox="0 0 20 28"><path d="M16 2 4 14l12 12" fill="none" stroke="var(--arrow)" stroke-width="5"/></svg>
  <svg class="arrow" style="left:876px;top:184px" width="20" height="28" viewBox="0 0 20 28"><path d="M4 2l12 12L4 26" fill="none" stroke="var(--arrow)" stroke-width="5"/></svg>
</section>

<div class="band-gap"></div>

<section class="dealers">
  <h2>Get To Know our Beautiful <span>Dealers</span></h2>
  <svg class="arrow" style="left:86px;top:75px" width="16" height="24" viewBox="0 0 16 24"><path d="M13 2 4 12l9 10" fill="none" stroke="var(--arrow)" stroke-width="4"/></svg>
  <div class="dealer-tile" style="left:129px"></div>
  <div class="dealer-tile" style="left:282px"></div>
  <div class="dealer-tile" style="left:435px"></div>
  <div class="dealer-tile" style="left:587px"></div>
  <div class="dealer-tile" style="left:740px"></div>
  <svg class="arrow" style="left:896px;top:75px" width="16" height="24" viewBox="0 0 16 24"><path d="M3 2l9 10-9 10" fill="none" stroke="var(--arrow)" stroke-width="4"/></svg>
  <p>They Will Ensure Your Players are <span>Smiling</span> Even when Losing!</p>
</section>

<section class="panel news">
  <h3>Latest news</h3>
  <ul>
    <li>| CTS featured in CSA Latin America 2011 in Panama, <span>2011.03.09</span></li>
    <li>| 15 units of kiosk delivered to Mexico &nbsp;<span>2010.06.12</span></li>
    <li>| "NORTH STAR" set to implement Live Dealer product, <span>2010.05.10</span></li>
    <li>| New High Definition video equipment placed in studio, <span>2010.05.06</span></li>
    <li>| Hours of operation extended, <span>2010.04.26</span></li>
  </ul>
  <span class="more">View more...</span>
</section>

<section class="panel about">
  <h3>Who we are...</h3>
  <p>&nbsp;&nbsp;&nbsp;&nbsp;&nbsp;&nbsp;&nbsp;&nbsp;Crown Table Studios is a leader among online casino software providers.<br>
  &nbsp;&nbsp;&nbsp;&nbsp;&nbsp;&nbsp;&nbsp;&nbsp;Our team of expert internet casino software developers, managers and marketers are here to ensure that any project you need, is a project Crown Table Studios can deliver. Our Casino services and consulting solutions can take your business to the next level.<br>
  &nbsp;&nbsp;&nbsp;&nbsp;&nbsp;&nbsp;&nbsp;&nbsp;Our online casino software licensing can help any start up achieve the quickest and most secure return on investment.</p>
  <span class="more">Read more...</span>
</section>

<footer class="site-footer">
  <div class="footer-call">Call Toll Free 1-xxx-xxx-xxxx and get a<br>FREE Demo of our Software and Solutions</div>
  <div class="footer-rule"></div>
  <div class="copyright">© 2008-2011 Crown Table Studios</div>
</footer>
</body>
</html>
```